I need 2 flyers designed for my business

Both can be similar in design and will have different purposes. I need an education based flyer and I need a government based flyer. The focus of the flyer will be software on the front and services on the back.
These all need to be 8.5x 11 in dimension (they can be full bleed). I would like to be able to print these out if needed. The design needs to look good with our website > www.brintalo.com

The software details are on the website.

```html
<!DOCTYPE html>
<html lang="en">
<head>
<meta charset="utf-8">
<title>Meridian Works – Service Flyers</title>
<link rel="stylesheet" href="https://fonts.googleapis.com/css2?family=Roboto:ital,wght@0,400;0,500;0,700;1,700&display=swap">
<style>
  :root {
    --gold: #dc9a18;
    --gold-pill: #f6c13c;
    --maroon: #7a1620;
    --maroon-body: #8a2230;
    --brand-red: #8c1b24;
    --heading-red: #a3172b;
    --ink: #1f1f1f;
    --white: #ffffff;
  }
  * { box-sizing: border-box; margin: 0; padding: 0; }
  html, body { width: 1200px; height: 1200px; overflow: hidden; background: var(--white); }
  body { position: relative; font-family: "Roboto", Arial, sans-serif; color: var(--white); }

  .flyer {
    position: absolute; top: 254px; width: 668px; height: 865px;
    transform: scale(0.8); transform-origin: top left; overflow: hidden; background: var(--white);
  }
  .flyer--front { left: 46px; }
  .flyer--back { left: 621px; }

  .top-band { position: absolute; left: 0; top: 0; width: 100%; height: 16px; }
  .flyer--front .top-band { background: var(--gold); }
  .flyer--back .top-band { background: linear-gradient(90deg, var(--maroon), #9b2a36); }

  .brand { position: absolute; left: 18px; top: 32px; display: flex; align-items: center; gap: 12px; }
  .brand-mark { width: 54px; height: 54px; background: var(--brand-red); }
  .brand-name { font-weight: 700; font-size: 29px; line-height: 1.02; color: var(--brand-red); letter-spacing: 0.5px; }

  .hero-photo {
    position: absolute; left: 0; top: 122px; width: 100%; height: 743px;
    background: linear-gradient(180deg, #e08d2a 0%, #d4662a 45%, #b8392a 100%);
  }
  .service-graphic {
    position: absolute; left: 49px; top: 210px; width: 560px; height: 560px; border-radius: 50%;
    background: linear-gradient(135deg, #f7a25c 0%, #e8587a 45%, #8a5ad8 100%);
    border: 5px solid var(--white);
  }

  .contact { position: absolute; right: 16px; top: 30px; text-align: right; color: var(--ink); }
  .contact-title { font-style: italic; font-weight: 700; font-size: 19px; color: var(--heading-red); margin-bottom: 12px; }
  .contact-line { font-size: 19px; line-height: 1.3; display: flex; align-items: center; justify-content: flex-end; gap: 6px; }
  .contact-line svg { width: 18px; height: 18px; color: var(--heading-red); }

  .body-photo {
    position: absolute; left: 0; top: 122px; width: 100%; height: 743px;
    background: radial-gradient(ellipse at 70% 80%, #9d3440 0%, var(--maroon-body) 55%, #7e1c28 100%);
  }
  .service-row { position: absolute; left: 17px; width: 634px; display: grid; grid-template-columns: 231px 233px 170px; }
  .divider { position: absolute; left: 17px; width: 634px; border-top: 1px dotted rgba(255,255,255,0.7); }
  .service-intro .service-title { display: flex; align-items: center; gap: 8px; font-size: 16px; font-weight: 500; margin-bottom: 10px; }
  .service-intro .service-title svg { width: 40px; height: 40px; color: var(--gold-pill); }
  .service-intro p { font-size: 9.6px; line-height: 1.5; width: 180px; }
  .col-heading { font-size: 16px; font-weight: 500; margin: 8px 0 8px; }
  .list { list-style: none; font-size: 9.6px; line-height: 1.4; }
  .list li { padding: 2px 0 3px; border-bottom: 1px dotted rgba(255,255,255,0.7); }
  .list--benefits { width: 174px; }
  .list--plain li { border-bottom: none; padding: 0 0 9px; }
  .quote-pill {
    display: inline-block; margin-top: 6px; padding: 3px 8px; border-radius: 10px;
    background: var(--gold-pill); color: var(--maroon); font-size: 8.5px; font-weight: 700;
  }
  .hidden-defs { position: absolute; width: 0; height: 0; }
</style>
</head>
<body>

<svg class="hidden-defs" aria-hidden="true">
  <defs>
    <symbol id="icon-software" viewBox="0 0 40 40">
      <g fill="none" stroke="currentColor" stroke-width="1.6" stroke-linejoin="round">
        <rect x="5" y="8" width="30" height="20" rx="1.5"/>
        <path d="M20 28v5M12 34h16"/>
        <circle cx="20" cy="18" r="4"/>
      </g>
    </symbol>
    <symbol id="icon-scan" viewBox="0 0 40 40">
      <g fill="none" stroke="currentColor" stroke-width="1.6" stroke-linejoin="round">
        <path d="M4 18l16-7 16 7-16 7z"/>
        <path d="M4 24l16 7 16-7"/>
        <path d="M4 30l16 7 16-7"/>
      </g>
    </symbol>
    <symbol id="icon-storage" viewBox="0 0 40 40">
      <g fill="none" stroke="currentColor" stroke-width="1.6" stroke-linejoin="round">
        <rect x="5" y="16" width="30" height="20"/>
        <rect x="15" y="23" width="10" height="5"/>
      </g>
    </symbol>
    <symbol id="icon-shred" viewBox="0 0 40 40">
      <g fill="none" stroke="currentColor" stroke-width="1.6" stroke-linejoin="round">
        <rect x="5" y="12" width="30" height="12" rx="2"/>
        <path d="M12 24v12M17 24v12M22 24v12M27 24v12"/>
      </g>
    </symbol>
  </defs>
</svg>

<section class="flyer flyer--front">
  <div class="top-band"></div>
  <div class="brand">
    <span class="brand-mark"></span>
    <span class="brand-name">MERIDIAN<br>WORKS</span>
  </div>
  <div class="hero-photo" role="img" aria-label="Photo of a developer at a desk with code and charts on screens, tinted orange to red"></div>
  <div class="service-graphic" role="img" aria-label="Circular service cycle illustration: Software, Scanning, Storage and Shredding around a central Service hub"></div>
</section>

<section class="flyer flyer--back">
  <div class="top-band"></div>
  <div class="brand">
    <span class="brand-mark"></span>
    <span class="brand-name">MERIDIAN<br>WORKS</span>
  </div>
  <div class="contact">
    <div class="contact-title">SALES INQUIRIES TO</div>
    <div class="contact-line">(555) 014-2380
      <svg viewBox="0 0 24 24"><path fill="currentColor" d="M3 9c0-3 4-5 9-5s9 2 9 5l-1 2-4-1v-2c-2-1-6-1-8 0v2l-4 1zM6 13h12l2 7H4z"/></svg>
    </div>
    <div class="contact-line">help@brintalo.com
      <svg viewBox="0 0 24 24"><path fill="currentColor" d="M22 3L2 11l7 3 2 7 3-5 5 3z"/></svg>
    </div>
  </div>

  <div class="body-photo" role="img" aria-label="Photo of hands typing at a laptop, tinted deep maroon"></div>

  <div class="service-row" style="top:142px">
    <div class="service-intro">
      <div class="service-title"><svg><use href="#icon-software"/></svg>Software</div>
      <p>Access all of your records - whether active or inactive - through ArchiveLens, our comprehensive records management software.</p>
    </div>
    <div>
      <div class="col-heading">Benefits</div>
      <ul class="list list--benefits">
        <li>Enjoy both web-based access to your records or access them on the go using our mobile app.</li>
        <li>Includes 3rd party integration tools.</li>
        <li>Protects records with disaster recovery and redundancy features.</li>
      </ul>
      <span class="quote-pill">Get A Quote</span>
    </div>
    <div>
      <div class="col-heading">ArchiveLens Provides:</div>
      <ul class="list">
        <li>Electronic forms</li>
        <li>Workflow automation</li>
        <li>Automated system/email notifications</li>
        <li>Full text search capabilities</li>
        <li>Audit tracking (including HIPAA)</li>
        <li>Redaction &amp; annotation capabilities</li>
      </ul>
    </div>
  </div>
  <div class="divider" style="top:309px"></div>

  <div class="service-row" style="top:318px">
    <div class="service-intro">
      <div class="service-title"><svg><use href="#icon-scan"/></svg>Scanning</div>
      <p>We scan your documents, converting them to digital archives so you can access them anytime.</p>
    </div>
    <div>
      <div class="col-heading">Benefits</div>
      <ul class="list list--benefits">
        <li>Reduces onsite storage</li>
        <li>Streamlines workflows</li>
        <li>Improves productivity</li>
        <li>Safeguards business intelligence</li>
        <li style="border-bottom:none">Maintains compliance</li>
      </ul>
      <span class="quote-pill">Get A Quote</span>
    </div>
    <div>
      <div class="col-heading">We Can Scan:</div>
      <ul class="list">
        <li>Standard office documents</li>
        <li>16mm and 35 mm roll microfilm</li>
        <li>Microfiche (Jackets or COM)</li>
        <li style="border-bottom:none">Large format documents/drawings</li>
      </ul>
    </div>
  </div>
  <div class="divider" style="top:474px"></div>

  <div class="service-row" style="top:480px">
    <div class="service-intro">
      <div class="service-title"><svg><use href="#icon-storage"/></svg>Storage</div>
      <p>Rediscover your office space by letting us store your records offsite.</p>
    </div>
    <div>
      <div class="col-heading">Benefits</div>
      <ul class="list list--benefits">
        <li>Free up valuable work space</li>
        <li>Have peace of mind, knowing your records are secure.</li>
        <li>Have peace of mind, knowing your records are secure.</li>
        <li>Enjoy personalized service via a dedicated Account Manager.</li>
        <li style="border-bottom:none">Reduce costs associated with storing records onsite.</li>
      </ul>
      <span class="quote-pill">Get A Quote</span>
    </div>
    <div>
      <div class="col-heading">Our Facility Is:</div>
      <ul class="list">
        <li>Locally-based, which means you can retrieve records easily.</li>
        <li>Fireproof, waterproof, and wind-free.</li>
        <li>Outfitted with motion-detect cameras.</li>
        <li>Staffed with surveillance personnel</li>
        <li style="border-bottom:none">Protected with surveillance software</li>
      </ul>
    </div>
  </div>
  <div class="divider" style="top:689px"></div>

  <div class="service-row" style="top:696px">
    <div class="service-intro">
      <div class="service-title"><svg><use href="#icon-shred"/></svg>Shredding</div>
      <p>Rediscover your office space by letting us store your records offsite.</p>
    </div>
    <div>
      <div class="col-heading">Benefits</div>
      <ul class="list list--benefits">
        <li>Protects important company information.</li>
        <li>Upholds customer confidentiality.</li>
        <li style="border-bottom:none">Reduces cost of managing information you no longer require.</li>
      </ul>
      <span class="quote-pill">Get A Quote</span>
    </div>
    <div>
      <div class="col-heading">Details &amp; Uses</div>
      <ul class="list list--plain">
        <li>Shredding can be one-time only or recurring, based on your needs.</li>
        <li>Ensures compliance with federal, state, industry, and credit card regulations to avoid penalties, fines, or even legal action.</li>
      </ul>
    </div>
  </div>
</section>

</body>
</html>
```